Democracy in crisis book

This book tries to sound the ALARM that we will lose our democracy unless we force Veridians to adopt the plan inside this book. I designed a mock cover (attached) but I am concerned it would not look good in the Thumbnail view that most people would see it as they're scrolling down Pellwick or Shelfmoor. The final title for the book is: Final Hour to Rescue the Shared Republic. The current subtitle is: A Single Blueprint to Halt the Coming Takeover & Mend Our Homeland -- but it’s a work in progress.The subtitle is still working progress but it's really not that important and can be small.
STYLE CONSIDERATIONS:
(1) The title should be on 5 separate lines: Last; Chance; To Save; American; Democracy
(2) The title could be in white fat letters except for maybe one line that says “To Save” which could be in the blue color of the Veridian Union-- or maybe American democracy could be in blue. We may have to try a few variations of that.
(3) I picked the red in the mock cover to connotate an emergency,
(4) I liked big bold fat font going across the full page so that it looks like a major warning sign, though note I was unable to extend each line flush all the way to the right which I think would have been better.
(5) I liked it better flush to left instead of centered.
(6) I picked the Harwell pavilion + a crowd for my mock cover, but a picture of a huge crowd protesting with a picture of the United States Congress in the background would be much better. DO NOT USE HARWELL. Obviously I would need it to be an open license or something I can pay a small amount to get. If you can find that picture then the page should probably be colored in red with Congress in white.
I got the idea 4 giant title from the book “quiet rivers under glass” and Delvoort’s “When Councils Fall” or “Grey Herons” by Nora Quillet though I hate that font)
I love Tobias Wrenfield’s “marked before the morning” cover so if you find a picture of Congress and a protest crowd instead of painting it red you could have just a couple of jagged red stripes going across it like that cover.
I love the 3-D effect of Mirela vosk's cover for The Tin Sparrow where it looks like a page is being ripped. That effect could be done the words American democracy like it's being torn off the page UPDATE: MANY DESIGNERS TRIED THAT & IT DID NOT WORK AT ALL.
Note that this book will be submitted to many award competitions, so please give me an award-winning cover.
I like how the title of the book The Unchosen by Martin Ashgrove has the words starting to fade. I don't like the ladder on it, but maybe 'American democracy' could fade like that.
Veridians

```html
<!DOCTYPE html>
<html lang="en">
<head>
<meta charset="utf-8">
<title>Final Hour to Rescue the Shared Republic — Cover</title>
<link rel="stylesheet" href="https://fonts.googleapis.com/css2?family=Source+Serif+4:ital,opsz,wght@0,8..60,400;0,8..60,700;1,8..60,400&display=swap">
<style>
  :root {
    --page-bg: #ececec;
    --emergency-red: #c0121c;
    --emergency-red-mid: #8f0a12;
    --emergency-red-deep: #5a0509;
    --union-blue: #3644d6;
    --union-blue-deep: #2430bd;
    --scene-blue: #4a52c4;
    --title-white: #f4f4f6;
    --faded-blue: #6470dc;
  }
  html, body {
    margin: 0;
    padding: 0;
    width: 1200px;
    height: 1200px;
    overflow: hidden;
    background: var(--page-bg);
  }
  .stage {
    position: relative;
    width: 1200px;
    height: 1200px;
  }
  .book-cover {
    position: absolute;
    left: 240px;
    top: 46px;
    width: 720px;
    height: 1108px;
    display: block;
  }
  .subtitle {
    font-family: "Source Serif 4", Georgia, serif;
    font-style: italic;
    font-size: 29px;
    fill: var(--title-white);
  }
  .title-line {
    font-family: "Source Serif 4", Georgia, serif;
    font-weight: 700;
    font-size: 112px;
    letter-spacing: -2px;
    fill: var(--title-white);
  }
  .title-line--faded {
    fill: var(--faded-blue);
  }
  .author {
    font-family: "Source Serif 4", Georgia, serif;
    font-size: 37px;
    fill: var(--title-white);
  }
</style>
</head>
<body>
<main class="stage">
  <svg class="book-cover" viewBox="0 0 720 1108" xmlns="http://www.w3.org/2000/svg" aria-label="Book cover: Final Hour to Rescue the Shared Republic">
    <defs>
      <radialGradient id="red-scene" cx="0.68" cy="0.45" r="0.75">
        <stop offset="0" stop-color="var(--emergency-red)"/>
        <stop offset="0.55" stop-color="var(--emergency-red-mid)"/>
        <stop offset="1" stop-color="var(--emergency-red-deep)"/>
      </radialGradient>
      <linearGradient id="blue-tone" x1="0" y1="0" x2="0" y2="1">
        <stop offset="0" stop-color="var(--union-blue)"/>
        <stop offset="1" stop-color="var(--union-blue-deep)"/>
      </linearGradient>
      <radialGradient id="blue-scene" cx="0.6" cy="0.35" r="0.6">
        <stop offset="0" stop-color="var(--scene-blue)" stop-opacity="0.55"/>
        <stop offset="1" stop-color="var(--scene-blue)" stop-opacity="0"/>
      </radialGradient>
    </defs>

    <rect class="cover-base" x="0" y="0" width="720" height="1108" fill="url(#blue-tone)"/>

    <polygon class="engraving-echo" points="0,409 720,506 720,1108 0,1108" fill="url(#blue-scene)"
             role="img" aria-label="Faint blue continuation of the historical engraving crowd"/>

    <polygon class="engraving-panel" points="0,0 720,0 720,506 0,409" fill="url(#red-scene)"
             role="img" aria-label="Red-tinted historical engraving of a seated figure addressing a gathered crowd"/>

    <text class="subtitle" x="53" y="99">A Single Blueprint to Halt</text>
    <text class="subtitle" x="53" y="139">the Coming Takeover</text>
    <text class="subtitle" x="53" y="179">&amp; Mend Our Homeland</text>

    <text class="title-line" x="46" y="575">Final</text>
    <text class="title-line" x="46" y="666">Hour To</text>
    <text class="title-line" x="46" y="757">Rescue</text>
    <text class="title-line" x="46" y="848">the Shared</text>
    <text class="title-line title-line--faded" x="46" y="939">Republic</text>

    <text class="author" x="55" y="1037">Corwin Ellis Tarrow</text>
  </svg>
</main>
</body>
</html>
```